Flyer für Hausreinigung
Zielgruppe
Hausverwaltungen, Hausbesitzer.
Aufgabenstellung
Ergebnis soll ein Winword-Dokument mit einem Firmenlogo (Vorschlag: Tintenklecks hellgrün/blau verlaufend mit orangem Besen/Wischer/oder Hand - andere Ideen sind willkommen!) sein, das ich noch um Firmenname/Adresse bzw. Empfängerdaten noch vervollständigen/individualisieren kann. Es soll bunt, aber nicht überladen sein, eventuell mit Stockfotos von lachenden/glücklich schauenden aktiven Menschen sein, jung dynamisch aber nicht flippig. Folgender Text sollte darin vorkommen, Umformulierungen und andere Ideen sind hochwillkommen:
Unser Ziel ist es eine Hausbetreuung fast wie ein Hausbesorger zu leisten, jedoch mit zusätzlichen Vorteilen:
· Der Vertrag ist jederzeit ohne Frist kündbar, ohne Angabe von Gründen!
· Reinigung 1 x pro Woche sowie zusätzliche Bedarfsreinigung
· Krankheits- und Urlaubsvertretung sind bereits inklusive.
· Haftpflichtversicherung über 1,5 Mio. Euro
· Inklusive Gartenbetreuung, Garage, Dachboden, Haustechnik
· Kontrollgänge, 7 x 24 h Erreichbarkeit für Mieter und Eigentümer, Handwerkerüberwachung, Notfallkoordination
· Winterbetreuung der Gehsteige täglich mindestens zwischen 6:00 und 22:00
· Inklusive aller Hilfsmittel und Materialien
· Fixpreis pro Monat.
Nach Möglichkeit soll das auf 1 A4-Seite Platz finden.

```html
<!DOCTYPE html>
<html lang="de">
<head>
<meta charset="utf-8">
<title>Harald Berger Hausbetreuung – Flyer</title>
<link rel="stylesheet" href="https://fonts.googleapis.com/css2?family=Open+Sans:ital,wght@0,400;0,700;1,600;1,700;1,800&display=swap">
<style>
  :root {
    --sky-top: #2a9fdc;
    --sky-mid: #9fd4ee;
    --sky-low: #c6e7f5;
    --navy: #1c3a66;
    --ink: #111418;
    --accent-blue: #2674b5;
    --logo-yellow: #f2cf1d;
    --footer-band: #d9c53c;
    --footer-band-dark: #c9b22a;
    --white: #ffffff;
  }
  * { margin: 0; padding: 0; box-sizing: border-box; }
  html, body { width: 848px; height: 1200px; overflow: hidden; }
  body { font-family: "Open Sans", Arial, sans-serif; background: var(--sky-low); }

  .flyer {
    position: relative;
    width: 848px;
    height: 1200px;
    overflow: hidden;
    background: linear-gradient(180deg, var(--sky-top) 0px, #58b6e4 180px, var(--sky-mid) 330px, var(--sky-low) 700px, var(--sky-low) 1200px);
  }
  .sky-swoosh { position: absolute; left: 0; top: 150px; width: 848px; height: 140px; }

  .brand {
    position: absolute; left: 298px; top: 84px;
    display: flex; align-items: center; gap: 8px;
  }
  .brand-square { width: 68px; height: 68px; background: var(--logo-yellow); border: 3px solid var(--white); }
  .brand-text { display: flex; flex-direction: column; line-height: 1; }
  .brand-name { font-weight: 700; font-size: 30px; color: var(--navy); letter-spacing: -0.5px; }
  .brand-tagline { font-weight: 400; font-size: 11px; color: var(--navy); margin-top: 3px; }

  .hand-photo {
    position: absolute; left: -20px; top: 258px; width: 370px; height: 345px;
    border-radius: 46% 54% 40% 60% / 50% 45% 55% 50%;
    background: linear-gradient(160deg, #4f8fd8 0%, #3e7fcc 40%, #e2b49a 70%, #d9a78c 100%);
    opacity: 0.9;
  }

  .headline, .benefit {
    position: absolute; white-space: nowrap;
    transform: rotate(3.5deg); transform-origin: left top;
  }
  .headline {
    display: block;
    font-style: italic; font-weight: 800; font-size: 27px; color: var(--navy);
    text-shadow: 0 0 6px rgba(255,255,255,0.7);
  }

  .benefits { list-style: none; }
  .benefit {
    font-style: italic; font-weight: 700; font-size: 16.5px; line-height: 25px; color: var(--ink);
    text-shadow: 0 0 4px var(--white), 0 0 8px var(--white);
  }
  .benefit-line { display: block; }
  .benefit.is-blue, .benefit .is-blue { color: var(--accent-blue); font-weight: 600; }

  .footer-band { position: absolute; left: 0; top: 1120px; width: 848px; height: 80px; }
  .footer-contact {
    position: absolute; top: 1155px; left: 0; width: 848px; height: 30px;
    font-style: italic; font-weight: 700; font-size: 17px; color: var(--ink);
  }
  .footer-contact span { position: absolute; top: 0; white-space: nowrap; }
</style>
</head>
<body>
<main class="flyer">
  <svg class="sky-swoosh" viewBox="0 0 848 140" preserveAspectRatio="none" aria-hidden="true">
    <path d="M0 70 C 200 20, 420 40, 560 60 C 680 78, 780 60, 848 40 L 848 70 C 760 95, 640 100, 520 85 C 380 70, 200 60, 0 100 Z" fill="rgba(255,255,255,0.75)"/>
    <path d="M0 105 C 220 70, 420 90, 600 100 C 720 106, 800 96, 848 86 L 848 120 C 700 130, 500 118, 300 112 C 180 110, 80 118, 0 130 Z" fill="rgba(255,255,255,0.35)"/>
  </svg>

  <header class="brand">
    <div class="brand-square"></div>
    <div class="brand-text">
      <span class="brand-name">Harald Berger</span>
      <span class="brand-tagline">Hausbetreuung</span>
    </div>
  </header>

  <div class="hand-photo" role="img" aria-label="Foto: Hand wischt mit einem blauen Mikrofasertuch über eine Fläche"></div>

  <h1>
    <span class="headline" style="left:364px; top:284px;">Unser Ziel ist es eine</span>
    <span class="headline" style="left:372px; top:321px;">Hausbetreuung fast wie ein</span>
    <span class="headline" style="left:394px; top:358px;">Hausbesorger zu leisten</span>
    <span class="headline" style="left:370px; top:395px;">jedoch mit zusätzlichen Vorteilen:</span>
  </h1>

  <ul class="benefits">
    <li class="benefit" style="left:355px; top:478px;">
      <span class="benefit-line">· Der Vertrag ist jederzeit ohne Frist kündbar, ohne</span>
      <span class="benefit-line" style="margin-left:9px;">Angabe von &nbsp;&nbsp;&nbsp; Gründen!</span>
    </li>
    <li class="benefit is-blue" style="left:303px; top:524px;">
      <span class="benefit-line">· Reinigung 1 x pro Woche sowie zusätzliche</span>
      <span class="benefit-line" style="margin-left:-2px;">Bedarfsreinigung</span>
    </li>
    <li class="benefit" style="left:351px; top:572px;">· Krankheits- und Urlaubsvertretung sind bereits inklusive.</li>
    <li class="benefit is-blue" style="left:273px; top:594px;">· Haftpflichtversicherung über 1,5 Mio. Euro</li>
    <li class="benefit" style="left:230px; top:614px;">· Inklusive Gartenbetreuung, Garage, Dachboden, Haustechnik</li>
    <li class="benefit is-blue" style="left:175px; top:640px;">
      <span class="benefit-line">· Kontrollgänge, 7 x 24 h Erreichbarkeit für Mieter und Eigentümer,</span>
      <span class="benefit-line" style="margin-left:5px;">Handwerkerüberwachung, Notfallkoordination</span>
    </li>
    <li class="benefit" style="left:137px; top:690px;">· Winterbetreuung der Gehsteige täglich mindestens zwischen <span class="is-blue">6:00 und 22:00</span></li>
    <li class="benefit is-blue" style="left:114px; top:716px;">· Inklusive aller Hilfsmittel und Materialien</li>
    <li class="benefit" style="left:97px; top:737px;">· Fixpreis pro Monat.</li>
  </ul>

  <svg class="footer-band" viewBox="0 0 848 80" preserveAspectRatio="none" aria-hidden="true">
    <path d="M0 14 C 250 0, 600 0, 848 12 L 848 80 L 0 80 Z" fill="var(--footer-band-dark)"/>
    <path d="M0 20 C 250 6, 600 6, 848 18 L 848 80 L 0 80 Z" fill="var(--footer-band)"/>
  </svg>
  <footer class="footer-contact">
    <span style="left:106px;">Lindenweg 4</span>
    <span style="left:294px;">Musterstadt</span>
    <span style="left:425px;">Tel: 0123456789</span>
    <span style="left:587px;">Email: info@berger-hb.at</span>
  </footer>
</main>
</body>
</html>
```